One Page / Executive Summary for Silverpine Executive Search

We would need an executive summary for our firm Silverpine Executive Search - like a small one pager which we can via PDF to our clients.
It should include like the file 23030 all Infos - Only Track Record needs to be complemented
But it should be designed much nicer than it is now - also open for new design situations but it should fit our website concept www.silverpinexs.io
It should also include a graph of the recruiting process - maybe draw a new one.?
We would need a very elegant, modern, slim design, it should look very female - it should not have a green color block on the top but be more sleek bright and with our bird
Target Market(s)
CEO, HR executives
Industry/Entity Type
HR Consultantcy
Other font styles liked:
- Calibri, cost or robotic condensed
Requirements
Must have
- sleek slim modern elegant design, ideally a white side with a frame or with our bird
Nice to have
- project progress on our website, female modern, elegant design, not too overloaded, possibility to complement our text
Should not have
- no petrol color block as on our website or as in our proposal, prefer a white background with our photo as a log,

```html
<!DOCTYPE html>
<html lang="en">
<head>
<meta charset="utf-8">
<title>Silverpine Executive Search – Executive Summary</title>
<link href="https://fonts.googleapis.com/css2?family=Poppins:wght@300;400;500;600;700&family=Roboto+Condensed:wght@500&display=swap" rel="stylesheet">
<style>
  :root{
    --teal:#1b6f7e;
    --teal-dark:#0d5766;
    --sky:#93cde0;
    --sky-pale:#c5e6f0;
    --mist:#dcecf1;
    --red:#e2483d;
    --ink:#2d2d2d;
    --grey:#4a4a4a;
    --white:#ffffff;
  }
  html,body{margin:0;padding:0;overflow:hidden;background:#ffffff;}
  .sheet{position:relative;width:800px;height:1200px;overflow:hidden;background:var(--white);font-family:'Poppins',sans-serif;color:var(--ink);}
  .abs{position:absolute;margin:0;}

  .brand{left:40px;top:98px;display:flex;align-items:center;gap:12px;}
  .brand-dot{width:34px;height:34px;border-radius:50%;background:var(--sky-pale);}
  .brand-name{font-family:'Poppins',sans-serif;font-weight:300;font-size:30px;letter-spacing:5px;color:var(--teal);}

  .about{left:455px;top:55px;width:345px;height:89px;box-sizing:border-box;border:2px solid var(--teal);border-right:none;border-radius:10px 0 0 10px;padding:12px 22px 0 9px;font-size:9.3px;line-height:12.3px;color:var(--ink);}

  .team{left:455px;top:160px;width:345px;height:212px;box-sizing:border-box;border:2px solid var(--sky);border-right:none;border-radius:10px 0 0 10px;overflow:hidden;}
  .team-head{height:37px;background:var(--sky);color:var(--white);font-weight:600;font-size:20px;line-height:37px;padding-left:22px;}
  .member{margin:0 60px 0 26px;padding:9px 0 8px;border-bottom:1px dashed var(--sky);}
  .member:last-child{border-bottom:none;}
  .member-name{font-weight:500;font-size:13.5px;line-height:17px;color:var(--ink);}
  .member-mail{font-size:11px;line-height:15px;color:var(--ink);display:flex;align-items:center;gap:6px;margin-top:1px;}

  .tagline{left:35px;top:190px;font-size:24px;line-height:31px;color:var(--grey);font-weight:400;}
  .never{left:35px;top:259px;font-size:27px;font-weight:700;color:var(--sky);}

  .value{top:322px;width:90px;text-align:center;}
  .value-icon{display:block;margin:0 auto 6px;}
  .value-label{font-size:14.5px;font-weight:500;color:var(--ink);letter-spacing:.3px;}
  .vsep{top:317px;height:63px;border-left:1px dashed var(--sky);}

  .rule-red{left:32px;top:400px;width:731px;height:0;border-top:1.5px solid var(--red);}

  .section-title{font-weight:700;color:var(--sky);font-size:22px;line-height:26px;}
  .service-title{font-weight:700;color:var(--teal);font-size:14px;line-height:17px;}
  .body-text{font-size:9.3px;line-height:11.8px;color:var(--ink);}

  .why-item{display:flex;gap:7px;font-size:9.3px;line-height:11.8px;color:var(--ink);}
  .why-item svg{flex:none;margin-top:2px;}

  .pill{top:722px;height:24px;border-radius:12px;font-size:12.5px;font-weight:500;color:var(--teal-dark);text-align:center;line-height:24px;}
  .pill-deep{background:var(--sky);}
  .pill-pale{background:var(--sky-pale);}

  .phase-name{font-weight:700;font-size:17px;line-height:19px;color:var(--grey);}
  .phase-sub{font-size:10px;line-height:12px;color:var(--grey);}
  .step{top:852px;width:130px;height:108px;}
  .step-line{position:absolute;left:0;top:14px;height:94px;border-left:1.5px solid #e3e8ea;}
  .step-icon{position:absolute;left:-2px;top:0;width:26px;height:26px;border-radius:50%;}
  .step-title{position:absolute;left:13px;top:32px;font-weight:600;font-size:12.5px;line-height:14px;color:var(--red);}
  .step-text{position:absolute;left:13px;font-size:9.3px;line-height:11.5px;color:var(--ink);width:118px;}

  .numbers{left:0;top:976px;width:403px;height:127px;background:var(--teal-dark);border-radius:0 18px 18px 0;color:var(--white);}
  .numbers-title{position:absolute;left:35px;top:8px;font-weight:600;font-size:19px;}
  .stat{position:absolute;top:40px;padding-left:9px;border-left:1px dashed rgba(255,255,255,.7);height:62px;}
  .stat-big{font-weight:700;font-size:26px;line-height:26px;}
  .stat-text{font-size:11px;line-height:13px;font-weight:300;}

  .track-item{display:flex;align-items:center;gap:9px;height:20px;font-weight:600;font-size:10.3px;color:var(--grey);white-space:nowrap;}

  .address{left:30px;top:1115px;display:flex;align-items:center;gap:6px;font-size:9.4px;font-weight:600;color:var(--ink);}

  .contact{left:25px;top:1139px;width:736px;height:31px;border-radius:16px;background:var(--mist);overflow:hidden;display:flex;align-items:center;}
  .contact-label{width:97px;height:31px;background:var(--sky);color:var(--teal-dark);font-weight:600;font-size:13px;line-height:31px;text-align:center;}
  .contact-item{position:absolute;top:0;height:31px;display:flex;align-items:center;gap:7px;font-family:'Roboto Condensed',sans-serif;font-weight:500;color:var(--ink);white-space:nowrap;}
  .contact-white{position:absolute;left:426px;top:0;width:310px;height:31px;background:var(--white);border-radius:16px;box-sizing:border-box;border:1px solid var(--mist);}
</style>
</head>
<body>
<div class="sheet">

  <div class="abs brand"><span class="brand-dot"></span><span class="brand-name">SILVERPINE</span></div>

  <p class="abs about">Silverpine was founded in 2021 and is a female-led Executive Search and Leadership Advisory firm - focused on high quality and diversity - devoted to connecting leaders with a diverse background and companies with one another.</p>

  <section class="abs team">
    <div class="team-head">Your Team</div>
    <div class="member">
      <div class="member-name">Dr. Clara Weston-Hale</div>
      <div class="member-mail"><svg width="11" height="8" viewBox="0 0 11 8"><rect width="11" height="8" fill="var(--sky)"/><path d="M0 0 L5.5 4.5 L11 0" fill="none" stroke="#fff" stroke-width="1"/></svg>cwh@silverpinexs.io</div>
    </div>
    <div class="member">
      <div class="member-name">Mara Lindqvist</div>
      <div class="member-mail"><svg width="11" height="8" viewBox="0 0 11 8"><rect width="11" height="8" fill="var(--sky)"/><path d="M0 0 L5.5 4.5 L11 0" fill="none" stroke="#fff" stroke-width="1"/></svg>ml@silverpinexs.io</div>
    </div>
    <div class="member">
      <div class="member-name">Lena Hartwig</div>
      <div class="member-mail"><svg width="11" height="8" viewBox="0 0 11 8"><rect width="11" height="8" fill="var(--sky)"/><path d="M0 0 L5.5 4.5 L11 0" fill="none" stroke="#fff" stroke-width="1"/></svg>lh@silverpinexs.io</div>
    </div>
  </section>

  <h1 class="abs tagline">So, they don’t wear<br>ties in the boardroom anymore.</h1>
  <p class="abs never">WE NEVER DID...</p>

  <div class="abs value" style="left:26px;">
    <svg class="value-icon" width="31" height="31" viewBox="0 0 31 31"><circle cx="15.5" cy="15.5" r="15.5" fill="var(--sky)"/><path d="M15.5 22 L9 15.5 A3.5 3.5 0 0 1 15.5 11 A3.5 3.5 0 0 1 22 15.5 Z" fill="var(--red)"/></svg>
    <div class="value-label">HONEST</div>
  </div>
  <div class="abs vsep" style="left:113px;"></div>
  <div class="abs value" style="left:123px;">
    <svg class="value-icon" width="31" height="31" viewBox="0 0 31 31"><circle cx="15.5" cy="15.5" r="15.5" fill="var(--sky)"/><circle cx="15.5" cy="11" r="4" fill="var(--red)"/><path d="M8.5 23 Q15.5 13 22.5 23 Z" fill="var(--teal-dark)"/></svg>
    <div class="value-label">PERSONAL</div>
  </div>
  <div class="abs vsep" style="left:221px;"></div>
  <div class="abs value" style="left:234px;width:100px;">
    <svg class="value-icon" width="31" height="31" viewBox="0 0 31 31"><circle cx="15.5" cy="15.5" r="15.5" fill="var(--sky)"/><path d="M15.5 19 L11 14.5 A2.6 2.6 0 0 1 15.5 11.5 A2.6 2.6 0 0 1 20 14.5 Z" fill="var(--red)"/><path d="M7 16 L12 23 M24 16 L19 23" stroke="var(--teal-dark)" stroke-width="2.2" stroke-linecap="round"/></svg>
    <div class="value-label">PRAGMATIC</div>
  </div>
  <div class="abs vsep" style="left:339px;"></div>
  <div class="abs value" style="left:337px;">
    <svg class="value-icon" width="31" height="31" viewBox="0 0 31 31"><circle cx="15.5" cy="15.5" r="15.5" fill="var(--sky)"/><circle cx="15.5" cy="15.5" r="8" fill="var(--teal-dark)"/><path d="M15.5 7.5 A8 8 0 0 1 23.5 15.5 L15.5 15.5 Z" fill="var(--red)"/></svg>
    <div class="value-label">DIVERSE</div>
  </div>

  <div class="abs rule-red"></div>

  <h2 class="abs section-title" style="left:35px;top:413px;">Services</h2>
  <h3 class="abs service-title" style="left:35px;top:443px;">Executive Search</h3>
  <p class="abs body-text" style="left:35px;top:461px;width:295px;">We are helping you to identify and hire highly qualified and experienced candidates for senior-level executive positions. Our goal is to identify the most qualified candidates and match them with the needs and culture of your company.</p>
  <div class="abs" style="left:372px;top:440px;height:92px;border-left:1px solid #d5dadc;"></div>
  <h3 class="abs service-title" style="left:431px;top:443px;">Leadership Advisory</h3>
  <p class="abs body-text" style="left:431px;top:461px;width:332px;">Our leadership advisory services are for management teams as well as HR-professionals and candidates. They are designed to help you, and your organization, to build strong and effective leadership skills and teams that can drive growth, innovation, and success.</p>

  <h2 class="abs section-title" style="left:35px;top:538px;">Why Us?</h2>
  <svg class="abs" style="left:0;top:0;" width="800" height="720" viewBox="0 0 800 720">
    <circle cx="155" cy="552" r="2.5" fill="var(--red)"/>
    <path d="M155 552 H757 Q767 552 767 562 V687 Q767 697 757 697 H50 Q40 697 40 687 V682" fill="none" stroke="var(--red)" stroke-width="1" stroke-dasharray="4 3"/>
    <circle cx="40" cy="682" r="2.5" fill="var(--red)"/>
  </svg>
  <div class="abs" style="left:36px;top:578px;width:330px;">
    <div class="why-item"><svg width="9" height="9" viewBox="0 0 9 9"><rect x=".5" y=".5" width="8" height="8" fill="none" stroke="var(--red)"/><path d="M2 4.5 L4 6.5 L8.5 1" fill="none" stroke="var(--teal)" stroke-width="1.3"/></svg><span>Longstanding experience with a passion for placing C-Level Executives</span></div>
    <div class="why-item" style="margin-top:12px;"><svg width="9" height="9" viewBox="0 0 9 9"><rect x=".5" y=".5" width="8" height="8" fill="none" stroke="var(--red)"/><path d="M2 4.5 L4 6.5 L8.5 1" fill="none" stroke="var(--teal)" stroke-width="1.3"/></svg><span>We work with you personally and act as an ambassador for our clients in the market</span></div>
    <div class="why-item" style="margin-top:12px;"><svg width="9" height="9" viewBox="0 0 9 9"><rect x=".5" y=".5" width="8" height="8" fill="none" stroke="var(--red)"/><path d="M2 4.5 L4 6.5 L8.5 1" fill="none" stroke="var(--teal)" stroke-width="1.3"/></svg><span>Engaging in at eye-level discussion beyond just placement and HR topics</span></div>
  </div>
  <div class="abs" style="left:400px;top:578px;width:345px;">
    <div class="why-item"><svg width="9" height="9" viewBox="0 0 9 9"><rect x=".5" y=".5" width="8" height="8" fill="none" stroke="var(--red)"/><path d="M2 4.5 L4 6.5 L8.5 1" fill="none" stroke="var(--teal)" stroke-width="1.3"/></svg><span>Structured, lean and, most importantly, transparent’ digital processes, with the opportunity of 24/7 self-update on search status in our online tool</span></div>
    <div class="why-item" style="margin-top:12px;"><svg width="9" height="9" viewBox="0 0 9 9"><rect x=".5" y=".5" width="8" height="8" fill="none" stroke="var(--red)"/><path d="M2 4.5 L4 6.5 L8.5 1" fill="none" stroke="var(--teal)" stroke-width="1.3"/></svg><span>Creative search approaches and comprehensive candidate evaluation</span></div>
    <div class="why-item" style="margin-top:12px;"><svg width="9" height="9" viewBox="0 0 9 9"><rect x=".5" y=".5" width="8" height="8" fill="none" stroke="var(--red)"/><path d="M2 4.5 L4 6.5 L8.5 1" fill="none" stroke="var(--teal)" stroke-width="1.3"/></svg><span>Referencing of candidates as part of the process; psychometrics on demand</span></div>
  </div>

  <h2 class="abs section-title" style="left:36px;top:719px;font-size:24px;">Industries</h2>
  <div class="abs pill pill-deep" style="left:181px;width:114px;">Healthcare</div>
  <div class="abs pill pill-pale" style="left:301px;width:88px;">Hospital</div>
  <div class="abs pill pill-deep" style="left:397px;width:114px;">Private Equity</div>
  <div class="abs pill pill-pale" style="left:518px;width:123px;">Venture Capital</div>
  <div class="abs pill pill-deep" style="left:649px;width:90px;">Education</div>

  <h2 class="abs section-title" style="left:35px;top:767px;">Recruiting Process</h2>
  <div class="abs" style="left:35px;top:796px;"><div class="phase-name">Phase 1</div><div class="phase-sub">Longlist</div></div>
  <svg class="abs" style="left:100px;top:802px;" width="210" height="8" viewBox="0 0 210 8"><path d="M0 4 H206 M202 1 L206 4 L202 7" fill="none" stroke="var(--red)" stroke-width="1"/></svg>
  <div class="abs" style="left:314px;top:796px;"><div class="phase-name">Phase 2</div><div class="phase-sub">Shortlist &amp; Focus<br>&amp; Interviews</div></div>
  <svg class="abs" style="left:420px;top:802px;" width="188" height="8" viewBox="0 0 188 8"><path d="M0 4 H184 M180 1 L184 4 L180 7" fill="none" stroke="var(--red)" stroke-width="1"/></svg>
  <div class="abs" style="left:609px;top:796px;"><div class="phase-name">Phase 3</div><div class="phase-sub">Closing</div></div>

  <div class="abs step" style="left:37px;">
    <span class="step-line"></span><span class="step-icon" style="background:var(--teal-dark);"></span>
    <div class="step-title">Kickoff</div>
    <div class="step-text" style="top:54px;">Discuss and agree on profile, position specification and target list.</div>
  </div>
  <div class="abs step" style="left:175px;">
    <span class="step-line"></span><span class="step-icon" style="background:var(--sky-pale);"></span>
    <div class="step-title">Research</div>
    <div class="step-text" style="top:54px;">Active and passive research, approach of potential candidates</div>
  </div>
  <div class="abs step" style="left:317px;">
    <span class="step-line"></span><span class="step-icon" style="background:var(--teal-dark);"></span>
    <div class="step-title">Interviews</div>
    <div class="step-text" style="top:54px;">Presentation of prioritised profiles, client interviews</div>
  </div>
  <div class="abs step" style="left:459px;">
    <span class="step-line"></span><span class="step-icon" style="background:var(--sky-pale);"></span>
    <div class="step-title">References</div>
    <div class="step-text" style="top:52px;">Assessments (optional), taking references</div>
  </div>
  <div class="abs step" style="left:610px;width:150px;">
    <span class="step-line"></span><span class="step-icon" style="background:var(--teal-dark);"></span>
    <div class="step-title">Final Candidate<br>Selection</div>
    <div class="step-text" style="top:68px;width:130px;">Contract negotiation and onboarding, feedback discussion</div>
  </div>

  <section class="abs numbers">
    <div class="numbers-title">By The Numbers</div>
    <div class="stat" style="left:37px;"><div class="stat-big">95%</div><div class="stat-text">retention rate<br>over the course<br>of two years</div></div>
    <div class="stat" style="left:149px;"><div class="stat-big">30+</div><div class="stat-text">placements<br>made with<br>Silverpine</div></div>
    <div class="stat" style="left:257px;top:34px;height:70px;"><div class="stat-big" style="font-size:21px;line-height:22px;">In total<br>20 years</div><div class="stat-text" style="margin-top:4px;">of experience in the<br>Executive search sector</div></div>
  </section>

  <h2 class="abs section-title" style="left:431px;top:970px;">Track Record</h2>
  <svg class="abs" style="left:0;top:970px;" width="800" height="150" viewBox="0 970 800 150">
    <path d="M584 984 H756 Q762 984 762 990 V1105 Q762 1111 756 1111 H443 Q437 1111 437 1105 V1014" fill="none" stroke="var(--teal-dark)" stroke-width="1" stroke-dasharray="4 3"/>
    <circle cx="437" cy="1012" r="2.5" fill="var(--teal-dark)"/>
  </svg>
  <div class="abs" style="left:446px;top:1005px;">
    <div class="track-item"><svg width="12" height="12" viewBox="0 0 12 12"><circle cx="6" cy="6" r="6" fill="var(--teal-dark)"/><path d="M3.2 6.2 L5.2 8 L8.8 4" fill="none" stroke="#fff" stroke-width="1.4"/></svg>CEO Sales &amp; Marketing, Consumer Health, Germany</div>
    <div class="track-item"><svg width="12" height="12" viewBox="0 0 12 12"><circle cx="6" cy="6" r="6" fill="var(--teal-dark)"/><path d="M3.2 6.2 L5.2 8 L8.8 4" fill="none" stroke="#fff" stroke-width="1.4"/></svg>CEO Europe, Radiology Chain, Germany</div>
    <div class="track-item"><svg width="12" height="12" viewBox="0 0 12 12"><circle cx="6" cy="6" r="6" fill="var(--teal-dark)"/><path d="M3.2 6.2 L5.2 8 L8.8 4" fill="none" stroke="#fff" stroke-width="1.4"/></svg>Female Partner, Deep Tech VC Fund, Germany,</div>
    <div class="track-item"><svg width="12" height="12" viewBox="0 0 12 12"><circle cx="6" cy="6" r="6" fill="var(--teal-dark)"/><path d="M3.2 6.2 L5.2 8 L8.8 4" fill="none" stroke="#fff" stroke-width="1.4"/></svg>COO, Health-Tech Startup, Germany</div>
    <div class="track-item"><svg width="12" height="12" viewBox="0 0 12 12"><circle cx="6" cy="6" r="6" fill="var(--teal-dark)"/><path d="M3.2 6.2 L5.2 8 L8.8 4" fill="none" stroke="#fff" stroke-width="1.4"/></svg>COO, Care Home chain PE owned, Germany</div>
  </div>

  <div class="abs address"><svg width="9" height="12" viewBox="0 0 9 12"><path d="M4.5 12 C1 7 0 5.8 0 4.5 A4.5 4.5 0 0 1 9 4.5 C9 5.8 8 7 4.5 12 Z" fill="var(--red)"/><circle cx="4.5" cy="4.5" r="1.7" fill="#fff"/></svg>Silverpine Executive Search GmbH, Birkenweg 14, 20095 Hamburg, Germany</div>

  <div class="abs contact">
    <div class="contact-label">Contact Us</div>
    <div class="contact-item" style="left:112px;font-size:13.5px;"><svg width="11" height="11" viewBox="0 0 11 11"><circle cx="5.5" cy="5.5" r="4.8" fill="none" stroke="var(--teal-dark)" stroke-width="1"/><path d="M0.7 5.5 H10.3 M5.5 0.7 V10.3" stroke="var(--teal-dark)" stroke-width="1"/><ellipse cx="5.5" cy="5.5" rx="2.2" ry="4.8" fill="none" stroke="var(--teal-dark)" stroke-width="1"/></svg>www.silverpinexs.io</div>
    <div class="abs" style="left:263px;top:5px;height:21px;border-left:1px solid #ffffff;"></div>
    <div class="contact-item" style="left:279px;font-size:11.5px;"><svg width="11" height="11" viewBox="0 0 11 11"><path d="M2.5 0.5 L4.5 3 L3.3 4.4 Q4.6 6.7 6.6 7.7 L8 6.5 L10.5 8.5 L9 10.5 Q3.5 10 0.5 2 Z" fill="var(--teal-dark)"/></svg>+49 151 20 555 018</div>
    <div class="contact-white"></div>
    <div class="contact-item" style="left:440px;font-size:11px;"><svg width="11" height="11" viewBox="0 0 11 11"><circle cx="5.5" cy="5.5" r="5.5" fill="var(--teal-dark)"/></svg>https://social.silverpinexs.io/company/silverpine/</div>
  </div>

</div>
</body>
</html>
```